Design a Brochure for Fenwick Lodges

I'd like a new brochure for my small cabin business. I'd like to be able to mail it in a standard business sized envelop. Tri-fold, front and back maybe. Keep it simple so it's an easy read. My website, which hopefully will give you an idea of what the cabins look like, and how I present them, is FenwickLodges.example. If the new brochure could have some of the same look and feel, or language, that would be nice to tie the two together. I do not get many requests for hard-copy brochures, but I do get some. I'd like to be able to give out a hard-copy when it is requested. Who knows, maybe I could replace my current homepage with the brochure (or part of it), to give the consumer a quick idea of what my small cabin business does. I believe my small cabin business is one of the best, maybe the best at its price-point, in the Marrow Ridge area. I want the business to be presented accurately, and very positively too. I have 100+ customer reviews too, they are on my website (testimonials page), we can use any of those quotes too. I presume I will get some sort of digital image that I can send over to PressLoop or some other service to actually print the flyers.

```html
<!DOCTYPE html>
<html lang="en">
<head>
<meta charset="utf-8">
<title>Fenwick Lodges – Brochure</title>
<link rel="stylesheet" href="https://fonts.googleapis.com/css2?family=Questrial&display=swap">
<style>
  :root {
    --backdrop: #d6d8db;
    --charcoal: #3a3a3c;
    --pink: #e6538f;
    --orange: #de8f2f;
    --orange-band: rgba(214, 128, 40, 0.92);
    --teal: #3aa8b8;
    --white: #ffffff;
    --photo-wood: #8a5a36;
    --photo-forest: #6f7f5a;
  }
  * { box-sizing: border-box; margin: 0; padding: 0; }
  html, body {
    width: 1200px; height: 800px; overflow: hidden;
    background: var(--backdrop);
    font-family: "Questrial", sans-serif;
    color: var(--white);
  }
  .brochure {
    position: absolute; left: 105px; top: 17px;
    width: 990px; height: 766px;
    background: var(--charcoal);
    overflow: hidden;
    box-shadow: 0 6px 18px rgba(0,0,0,0.25);
  }
  .block { position: absolute; }
  .photo { position: absolute; }
  .band {
    position: absolute; display: flex; align-items: center; justify-content: center;
    font-size: 24px; letter-spacing: 0.5px; color: var(--white);
  }
  .band--pink { background: var(--pink); }
  .band--orange { background: var(--orange-band); }
  .band--teal { background: var(--teal); }
  .copy { font-size: 12.5px; line-height: 1.45; }
  .copy p + p { margin-top: 6px; }

  /* Brand panel */
  .brand {
    left: 0; top: 0; width: 330px; height: 130px;
    background: var(--pink); padding: 16px;
  }
  .brand__box {
    width: 100%; height: 100%; background: var(--charcoal);
    display: flex; align-items: center; gap: 14px; padding: 0 22px;
  }
  .brand__square { width: 22px; height: 22px; background: var(--pink); flex: none; }
  .brand__name { font-size: 30px; line-height: 1; color: var(--white); }

  /* Left column */
  .cabin-photo { left: 0; top: 130px; width: 330px; height: 200px;
    background: linear-gradient(160deg, #b9c7b0 0%, #8d6a4a 45%, #a3303a 60%, #6d7a52 100%); }
  .cabin-title { left: 40px; top: 292px; width: 290px; height: 46px; }
  .details { left: 36px; top: 356px; width: 280px; }
  .details h2 { font-size: 13px; font-weight: normal; margin-bottom: 4px; }
  .details ul { list-style: none; font-size: 12.5px; line-height: 1.35; }
  .details li { position: relative; padding-left: 16px; }
  .details li::before {
    content: ""; position: absolute; left: 2px; top: 6px;
    width: 6px; height: 6px; background: var(--pink);
  }
  .intro {
    left: 0; top: 552px; width: 330px; height: 214px;
    background: var(--pink); padding: 22px 26px;
    font-size: 18px; line-height: 1.3;
  }

  /* Middle column */
  .tub-photo { left: 330px; top: 0; width: 330px; height: 190px;
    background: linear-gradient(180deg, #c9c2b4 0%, #6b5440 55%, #2e2a28 100%); }
  .tub-title { left: 345px; top: 152px; width: 300px; height: 46px; }
  .tub-copy {
    left: 330px; top: 198px; width: 330px; height: 170px;
    background: var(--orange); padding: 18px 22px; font-size: 13px;
  }
  .living-photo { left: 330px; top: 368px; width: 330px; height: 230px;
    background: linear-gradient(170deg, #5a3a24 0%, #9a6a44 50%, #3d2a1e 100%); }
  .living-title { left: 345px; top: 410px; width: 300px; height: 46px; }
  .living-copy { left: 352px; top: 614px; width: 290px; }

  /* Right column */
  .loft-copy { left: 684px; top: 22px; width: 286px; }
  .loft-title { left: 670px; top: 150px; width: 320px; height: 46px; }
  .loft-photo-a { left: 672px; top: 196px; width: 150px; height: 118px;
    background: linear-gradient(150deg, #b07a48 0%, #e0d3c2 60%, #7a4b2c 100%); }
  .loft-photo-b { left: 828px; top: 196px; width: 162px; height: 118px;
    background: linear-gradient(150deg, #9a6238 0%, #d7b48c 55%, #6e4328 100%); }
  .wildlife-photo { left: 660px; top: 320px; width: 330px; height: 240px;
    background: linear-gradient(180deg, #dfe4e6 0%, #9aa49a 45%, #5e7a45 100%); }
  .wildlife-title { left: 690px; top: 510px; width: 300px; height: 50px; }
  .wildlife-copy {
    left: 660px; top: 560px; width: 330px; height: 150px;
    background: var(--teal); padding: 18px 24px;
  }
</style>
</head>
<body>
  <main class="brochure">
    <!-- Left panel -->
    <header class="block brand">
      <div class="brand__box">
        <span class="brand__square"></span>
        <span class="brand__name">Fenwick<br>Lodges</span>
      </div>
    </header>
    <div class="photo cabin-photo" role="img" aria-label="Photo of the red-roofed log cabin among trees"></div>
    <div class="band band--pink cabin-title">Fenwick Woods</div>
    <section class="block details">
      <h2>A few details about Fenwick Woods</h2>
      <ul>
        <li>Sleeps six.</li>
        <li>Two bedrooms and two baths, one on each level.</li>
        <li>Indoor hot tub.</li>
        <li>Fireplace.</li>
        <li>Central air and heat.</li>
        <li>WiFi available.</li>
        <li>Wired phone service with free local and long distance.</li>
      </ul>
    </section>
    <section class="block intro">
      Fenwick Woods is a one of a kind cabin in the Marrow Ridge area. The upstairs loft bedroom is comfortably furnished with a king sized bed, private bath, and two balconies with a bridge connecting them.
    </section>

    <!-- Middle panel -->
    <div class="photo tub-photo" role="img" aria-label="Photo of the indoor hot tub beside tall windows"></div>
    <div class="band band--orange tub-title">Bubbly relaxing soak</div>
    <section class="block tub-copy copy">
      <p>After visiting the nearby State Parks, hiking through the woods, fishing, canoeing, bird watching, and antique shopping you're probably ready for a bubbly relaxing soak. Ahhh! The many windows surrounding the hot tub allow you to look out into the woods while you are getting some much needed R&amp;R.</p>
    </section>
    <div class="photo living-photo" role="img" aria-label="Photo of the living area with stone fireplace and log staircase"></div>
    <div class="band band--orange living-title">Comfortably Furnished</div>
    <section class="block living-copy copy">
      <p>The living area is comfortably furnished and tastefully appointed with a separate dining area and cozy fireplace.</p>
      <p>Large flat-screen TVs, satellite TV service, DVD too.</p>
      <p>You can watch the game or your favorite movie, it's all up to you.</p>
    </section>

    <!-- Right panel -->
    <section class="block loft-copy copy">
      <p>The upstairs loft bedroom is comfortably furnished with a king size bed, private bath, a reading nook, and two balconies with a bridge between them.</p>
      <p>Our guests tell us they sleep so soundly in this comfortable bed, hopefully you will too.</p>
    </section>
    <div class="band band--pink loft-title">The upstairs loft bedroom</div>
    <div class="photo loft-photo-a" role="img" aria-label="Photo of the loft bedroom with king size bed"></div>
    <div class="photo loft-photo-b" role="img" aria-label="Photo of the loft reading nook"></div>
    <div class="photo wildlife-photo" role="img" aria-label="Photo of deer among birch trees on the property"></div>
    <div class="band band--teal wildlife-title">Lots of wildlife</div>
    <section class="block wildlife-copy copy">
      <p>It's always fun to see some deer, raccoon, chipmunks, fox, humming birds, birds of prey, turkey, and many other bird species.</p>
      <p>You just never know what wildlife you'll see on our large and very secluded property.</p>
    </section>
  </main>
</body>
</html>
```